Website for Nonprofit for kids whose parents have been wounded

We need a web design for a nonprofit that serves children who have been severely burned as well as those whose parents have been wounded during military service. We will be based out of hospitals and will need a format that will encourage trust, safety, and respect. We are stick with a lot of red white and blue. We will also be looking to have a space for donations.

Target Market(s)

Kids and parents of military veterans

Industry/Entity Type

Non Profit

Number of Pages Required

5+ page

Font styles to use
Serif
Decorative

Colors
ec1f27
ffffff
0255a3

Requirements
Must have
• Be both appealing to children and adults. Create a reputable face for our organization. We need an area for donations.
Nice to have
• Something unique

```html
<!DOCTYPE html>
<html lang="en">
<head>
<meta charset="utf-8">
<title>Brave Kids — Home</title>
<link href="https://fonts.googleapis.com/css2?family=Open+Sans:wght@400;600;700&family=Oswald:wght@400;500&display=swap" rel="stylesheet">
<style>
:root{
  --red:#ec1f27;
  --blue:#0255a3;
  --navy:#0d1a2e;
  --navy-deep:#08111f;
  --white:#ffffff;
  --ink:#333a44;
  --muted:#6d7480;
  --line:#dfe3e8;
  --paper:#f1f2f4;
}
*{box-sizing:border-box;margin:0;padding:0}
html,body{width:692px;height:1200px;overflow:hidden;background:var(--white)}
body{font-family:"Open Sans",Arial,sans-serif;color:var(--ink)}
.page{position:relative;width:692px;height:1200px;overflow:hidden}

/* header */
.site-header{position:absolute;top:0;left:0;width:692px;height:34px;background:var(--white);z-index:2}
.brand{position:absolute;left:22px;top:10px;font-weight:600;font-size:11px;color:var(--ink);letter-spacing:.2px;white-space:nowrap}
.main-nav{position:absolute;left:254px;top:14px;display:flex;gap:20px;font-size:6px;font-weight:600;color:var(--ink);white-space:nowrap}
.main-nav .active{color:var(--red)}
.contact-line{position:absolute;right:60px;top:12px;display:flex;gap:12px;font-size:6px;color:var(--muted);white-space:nowrap}
.contact-line span{display:flex;align-items:center;gap:3px}
.search-btn{position:absolute;right:20px;top:9px;width:16px;height:14px;background:#3b3f46;display:flex;align-items:center;justify-content:center}

/* hero */
.hero{position:absolute;top:34px;left:0;width:692px;height:268px}
.hero-photo{position:absolute;inset:0;background:linear-gradient(180deg,#cfc3b2 0%,#a58a6e 45%,#6e4f38 100%)}
.hero-copy{position:absolute;top:185px;left:0;width:692px;text-align:center;color:var(--white)}
.hero-copy h1{font-weight:400;font-size:14px;letter-spacing:.4px}
.hero-copy p{font-size:5.5px;margin-top:3px}
.donate-bar{position:absolute;left:70px;top:262px;width:553px;height:26px;background:var(--white);border:1px solid var(--line);display:flex;align-items:center;gap:8px;padding:0 8px;z-index:3}
.donate-bar .field{width:102px;height:14px;border:1px solid var(--line);font-size:5.5px;color:var(--muted);padding:3px 4px;white-space:nowrap}
.donate-bar .donate-now{margin-left:auto;height:15px;width:104px;background:var(--red);color:var(--white);font-size:6.5px;font-weight:700;display:flex;align-items:center;justify-content:center;gap:10px;white-space:nowrap}

/* features */
.features{position:absolute;top:325px;left:78px;width:540px;display:flex;gap:30px}
.feature{display:flex;gap:7px;width:160px}
.feature-icon{flex:none;width:26px;height:26px;border-radius:50%;border:2px solid var(--red);display:flex;align-items:center;justify-content:center}
.feature-icon.blue{border-color:var(--blue)}
.feature-icon i{width:16px;height:16px;border-radius:50%;background:var(--red);display:block}
.feature-icon.blue i{background:var(--blue)}
.feature h3{font-size:7px;font-weight:700;color:var(--ink)}
.feature p{font-size:5px;line-height:1.5;color:var(--muted);margin-top:2px}

/* about */
.about{position:absolute;top:405px;left:0;width:692px;text-align:center}
.section-title{font-family:"Oswald",Arial,sans-serif;font-weight:400;font-size:22px;color:var(--ink);letter-spacing:.5px}
.about-text{width:380px;margin:12px auto 0;font-size:5.3px;line-height:1.6;color:var(--muted)}
.btn-red{display:inline-block;margin-top:14px;background:var(--red);color:var(--white);font-size:6px;font-weight:600;padding:5px 12px}

/* donate for them */
.gallery{position:absolute;top:560px;left:0;width:692px;height:436px;background:var(--paper)}
.gallery .section-title{position:absolute;top:30px;width:692px;text-align:center}
.gallery-sub{position:absolute;top:67px;width:692px;text-align:center;font-size:5.5px;color:var(--muted);letter-spacing:.3px}
.tiles{position:absolute;top:110px;left:82px;display:grid;grid-template-columns:172px 162px 166px;grid-template-rows:152px 156px;gap:10px 13px}
.tile{position:relative}
.tile.t1{background:linear-gradient(160deg,#3e8fd0,#2a6fae)}
.tile.t2{background:linear-gradient(160deg,#8a7565,#4e3f35)}
.tile.t3{background:linear-gradient(160deg,#d9c6b4,#9c7e66)}
.tile.t4{background:linear-gradient(160deg,#6d4a35,#3a2619)}
.tile.t5{background:linear-gradient(160deg,#b3a596,#6a5c50)}
.tile.t6{background:linear-gradient(160deg,#c7a98c,#8a6a4e)}
.zoom{position:absolute;left:76px;top:66px;width:20px;height:20px;border:1px solid rgba(255,255,255,.8);display:flex;align-items:center;justify-content:center}

/* footer */
.site-footer{position:absolute;top:996px;left:0;width:692px;height:204px;background:var(--navy);color:#c6ccd6}
.footer-col{position:absolute;top:34px}
.footer-col h4{font-size:7px;font-weight:700;color:var(--white);margin-bottom:9px;letter-spacing:.3px;white-space:nowrap}
.footer-col ul{list-style:none}
.footer-col li{font-size:5.5px;line-height:1.9;display:flex;align-items:center;gap:5px;white-space:nowrap}
.footer-col li::before{content:"";width:3px;height:3px;border-radius:50%;background:#c6ccd6}
.col-menu{left:80px}
.col-links{left:196px}
.col-news{left:341px;width:120px}
.col-news p{font-size:5.5px;margin-bottom:5px}
.col-news .input{width:95px;height:11px;background:var(--white);font-size:5px;color:var(--muted);padding:2px 4px;margin-bottom:4px}
.col-news .send{width:40px;height:12px;background:var(--red);color:var(--white);font-size:6px;font-weight:700;display:flex;align-items:center;justify-content:center}
.col-touch{left:512px;width:100px}
.socials{display:flex;gap:4px}
.socials span{width:11px;height:11px;border-radius:50%;background:#aeb6c2}
.footer-brand{margin-top:14px;font-weight:600;font-size:9px;color:var(--white);white-space:nowrap}
.copyright{position:absolute;bottom:0;left:0;width:692px;height:18px;background:var(--navy-deep);font-size:5px;text-align:center;line-height:18px;color:#9aa3b0}
</style>
</head>
<body>
<div class="page">

  <header class="site-header">
    <div class="brand">Brave Kids</div>
    <nav class="main-nav">
      <span class="active">HOME</span><span>WHO WE ARE</span><span>WHAT WE DO</span><span>DONATE</span><span>CONTACT</span>
    </nav>
    <div class="contact-line">
      <span><svg width="6" height="6" viewBox="0 0 10 10"><path d="M2 1l2 2-1 1.5a6 6 0 0 0 2.5 2.5L7 6l2 2-1.5 1.5C4 9 1 6 .5 2z" fill="#6d7480"/></svg>555 018 4420</span>
      <span><svg width="7" height="5" viewBox="0 0 10 7"><rect x=".5" y=".5" width="9" height="6" fill="none" stroke="#6d7480"/><path d="M.5.5 5 4 9.5.5" fill="none" stroke="#6d7480"/></svg>hello@bravekids.org</span>
    </div>
    <div class="search-btn"><svg width="8" height="8" viewBox="0 0 10 10"><circle cx="4" cy="4" r="3" fill="none" stroke="#fff" stroke-width="1.3"/><path d="M6.3 6.3 9 9" stroke="#fff" stroke-width="1.3"/></svg></div>
  </header>

  <section class="hero">
    <div class="hero-photo" role="img" aria-label="Photo of three smiling children standing together outdoors"></div>
    <div class="hero-copy">
      <h1>LOREM IPSUM IS SIMPLY DUMMY</h1>
      <p>Lorem Ipsum is simply dummy text of the printing and typesetting industry. Lorem Ipsum has been the standard.</p>
    </div>
  </section>

  <form class="donate-bar">
    <div class="field">First Name</div>
    <div class="field">Last Name</div>
    <div class="field">Email Address</div>
    <div class="field">Amount</div>
    <div class="donate-now">DONATE NOW
      <svg width="7" height="6" viewBox="0 0 10 8"><path d="M0 4h8M5 1l3 3-3 3" stroke="#fff" stroke-width="1.4" fill="none"/></svg>
    </div>
  </form>

  <section class="features">
    <div class="feature">
      <div class="feature-icon"><i></i></div>
      <div><h3>OUR MISSION</h3><p>Lorem Ipsum is simply dummy text of the printing and typesetting industry. Lorem Ipsum has been the industry's standard.</p></div>
    </div>
    <div class="feature">
      <div class="feature-icon blue"><i></i></div>
      <div><h3>WE CARE</h3><p>Lorem Ipsum is simply dummy text of the printing and typesetting industry. Lorem Ipsum has been the industry's standard.</p></div>
    </div>
    <div class="feature">
      <div class="feature-icon"><i></i></div>
      <div><h3>DONATE</h3><p>Lorem Ipsum is simply dummy text of the printing and typesetting industry. Lorem Ipsum has been the industry's standard.</p></div>
    </div>
  </section>

  <section class="about">
    <h2 class="section-title">ABOUT US</h2>
    <p class="about-text">Lorem Ipsum is simply dummy text of the printing and typesetting industry. Lorem Ipsum has been the industry's standard dummy text ever since when an unknown printer took a galley of type and scrambled it to make a type specimen book. It has survived not only five centuries but also the leap into electronic typesetting, remaining essentially unchanged.</p>
    <span class="btn-red">VIEW MORE</span>
  </section>

  <section class="gallery">
    <h2 class="section-title">DONATE FOR THEM</h2>
    <p class="gallery-sub">OUR SERVICES FOR CHILDREN WHOSE PARENTS HAVE BEEN WOUNDED DURING MILITARY SERVICE</p>
    <div class="tiles">
      <div class="tile t1" role="img" aria-label="Photo of a child, shown with a blue hover overlay">
        <div class="zoom"><svg width="10" height="10" viewBox="0 0 10 10"><circle cx="4" cy="4" r="3" fill="none" stroke="#fff" stroke-width="1.2"/><path d="M6.3 6.3 9 9" stroke="#fff" stroke-width="1.2"/></svg></div>
      </div>
      <div class="tile t2" role="img" aria-label="Photo of hands reaching toward each other"></div>
      <div class="tile t3" role="img" aria-label="Photo of a young girl"></div>
      <div class="tile t4" role="img" aria-label="Close-up photo of a child"></div>
      <div class="tile t5" role="img" aria-label="Photo of a boy standing outdoors"></div>
      <div class="tile t6" role="img" aria-label="Photo of a smiling child"></div>
    </div>
  </section>

  <footer class="site-footer">
    <div class="footer-col col-menu">
      <h4>MAIN MENU</h4>
      <ul><li>Home</li><li>Who we are</li><li>What we do</li><li>Donate</li><li>Contact</li></ul>
    </div>
    <div class="footer-col col-links">
      <h4>QUICK LINK</h4>
      <ul><li>Customer Policy</li><li>Our Policy</li><li>Terms and conditions of use</li><li>Secure payment</li><li>Sitemap</li></ul>
    </div>
    <div class="footer-col col-news">
      <h4>NEWSLETTER</h4>
      <p>Lorem ipsum dolor sit amet</p>
      <div class="input">Your Name</div>
      <div class="input">Email Id</div>
      <div class="send">SEND</div>
    </div>
    <div class="footer-col col-touch">
      <h4>GET IN TOUCH</h4>
      <div class="socials"><span></span><span></span><span></span><span></span></div>
      <div class="footer-brand">Brave Kids</div>
    </div>
    <div class="copyright">Copyright © 2015 Brave Kids. All rights reserved</div>
  </footer>

</div>
</body>
</html>
```